New Summit Tile Billboard at HQ

Looking to design a catchy image / theme for a billboard located just above our corporate HQ showroom and warehouse, along the service road of a 6-lane highway. Billboard measures 8ft x 24 ft. Would like to highlight that the store location is directly beneath the sign.

We are a retail and wholesale business selling premium flooring, ready to assemble cabinets, and granite countertops. See image ideas attached. Our information:
NAME: Summit Tile, Cabinets, Countertops
ADDRESS: 417 W. Hwy 82, Duncanville, TX 75284
WEBSITE: www.summittilehub.example
PHONE: 972-8-TILEUP (972-845-3887)

```html
<!DOCTYPE html>
<html lang="en">
<head>
<meta charset="utf-8">
<title>Summit Tile Billboard</title>
<link rel="stylesheet" href="https://fonts.googleapis.com/css2?family=Montserrat:wght@500;600;700;800;900&family=Kaushan+Script&display=swap">
<style>
  :root{
    --page:#c9c9c9;
    --white:#ffffff;
    --charcoal:#2a2c33;
    --green:#72c04a;
    --green-dark:#4f9a2c;
    --red:#ec3b24;
    --ink:#232428;
  }
  *{box-sizing:border-box;margin:0;padding:0}
  html,body{width:1200px;height:1092px;overflow:hidden;background:var(--page)}
  body{position:relative;font-family:"Montserrat",sans-serif;color:var(--ink)}
  .billboard{position:absolute;left:40px;top:359px;width:1120px;height:373px;background:var(--white);box-shadow:-6px 8px 10px rgba(0,0,0,.35);overflow:hidden}
  .billboard-shapes{position:absolute;inset:0}
  .t{position:absolute;white-space:nowrap;line-height:1}
  .brand{left:40px;top:38px;display:flex;align-items:center;gap:10px;font-weight:800;font-size:31px;color:var(--ink)}
  .brand-mark{width:22px;height:22px;background:var(--green)}
  .tagline{left:38px;top:121px;font-weight:700;font-size:19px;line-height:1.2;color:var(--charcoal)}
  .free{left:38px;top:187px;font-weight:900;font-size:58px;letter-spacing:1px;color:var(--ink)}
  .in-home{left:38px;top:240px;font-family:"Kaushan Script",cursive;font-size:44px;color:var(--green)}
  .consult{left:38px;top:293px;font-weight:600;font-size:20.5px;color:var(--ink)}
  .quote{left:43px;top:322px;width:161px;height:28px;border-radius:14px;background:var(--red);color:var(--white);font-weight:700;font-size:15.5px;display:flex;align-items:center;justify-content:center}
  .service{font-weight:700;font-size:29px;color:var(--white)}
  .s-floors{left:356px;top:38px}
  .s-cabinets{left:530px;top:36px}
  .s-counter{left:336px;top:84px}
  .about{left:278px;top:130px;font-weight:500;font-size:16px;line-height:1.18;color:var(--white);white-space:normal;width:400px}
  .here{left:280px;top:214px;font-weight:700;font-size:17px;letter-spacing:.3px;color:var(--charcoal)}
  .address{left:314px;top:258px;font-weight:800;font-size:19px;color:var(--charcoal)}
  .phone{left:325px;top:299px;font-weight:500;font-size:16.5px;color:var(--charcoal)}
  .web{left:334px;top:331px;font-weight:500;font-size:16.5px;color:var(--charcoal)}
</style>
</head>
<body>
<section class="billboard">
  <svg class="billboard-shapes" viewBox="0 0 1120 373" width="1120" height="373">
    <defs>
      <clipPath id="info-area"><path d="M306 0 Q200 186 306 373 L760 373 Q672 186 760 0 Z"/></clipPath>
      <linearGradient id="room" x1="0" y1="0" x2="1" y2="1">
        <stop offset="0" stop-color="#d9c27a"/><stop offset=".45" stop-color="#c9863e"/><stop offset="1" stop-color="#e0913f"/>
      </linearGradient>
      <linearGradient id="lounge" x1="0" y1="0" x2="0" y2="1">
        <stop offset="0" stop-color="#b5633a"/><stop offset="1" stop-color="#d88a44"/>
      </linearGradient>
      <linearGradient id="kitchen" x1="0" y1="0" x2="0" y2="1">
        <stop offset="0" stop-color="#cdd6de"/><stop offset=".6" stop-color="#e8d6c2"/><stop offset="1" stop-color="#e9b69a"/>
      </linearGradient>
    </defs>
    <rect class="band" x="0" y="112" width="262" height="61" fill="var(--green)"/>
    <g clip-path="url(#info-area)">
      <rect x="0" y="0" width="1120" height="373" fill="var(--green)"/>
      <rect x="0" y="0" width="1120" height="222" fill="var(--charcoal)"/>
      <rect x="230" y="205" width="203" height="34" rx="17" fill="var(--green)" stroke="var(--white)" stroke-width="1.5"/>
    </g>
    <line x1="433" y1="222" x2="740" y2="222" stroke="var(--white)" stroke-width="1.5"/>
    <line x1="316" y1="286" x2="678" y2="286" stroke="var(--charcoal)" stroke-width="1.5"/>
    <path d="M738 0 Q650 186 738 373 L1120 373 L1120 0 Z" fill="url(#room)" role="img" aria-label="Bedroom interior with warm hardwood flooring"/>
    <path d="M732 0 Q644 186 732 373" fill="none" stroke="var(--white)" stroke-width="1.5"/>
    <circle cx="843" cy="286" r="72" fill="url(#lounge)" stroke="var(--white)" stroke-width="4" role="img" aria-label="Living room with wood floor"/>
    <circle cx="1013" cy="286" r="72" fill="url(#kitchen)" stroke="var(--white)" stroke-width="4" role="img" aria-label="Kitchen with granite countertop"/>
    <g class="icon-floors">
      <circle cx="319" cy="49" r="18" fill="var(--green)" stroke="#a6de84" stroke-width="2"/>
      <path d="M310 56 L313 44 H325 L328 56 Z M312 50 H326 M319 44 V56" fill="none" stroke="var(--white)" stroke-width="2"/>
    </g>
    <g class="icon-cabinets">
      <circle cx="498" cy="50" r="18" fill="var(--green)" stroke="#a6de84" stroke-width="2"/>
      <rect x="490" y="41" width="16" height="17" fill="none" stroke="var(--white)" stroke-width="2"/>
      <line x1="498" y1="41" x2="498" y2="58" stroke="var(--white)" stroke-width="2"/>
    </g>
    <g class="icon-countertops">
      <circle cx="303" cy="99" r="18" fill="var(--green)" stroke="#a6de84" stroke-width="2"/>
      <rect x="294" y="96" width="18" height="12" fill="var(--white)"/>
      <rect x="293" y="92" width="20" height="3" fill="var(--white)"/>
      <rect x="301" y="87" width="3" height="5" fill="var(--white)"/>
    </g>
    <path class="icon-pin" d="M292 282 C284 271 280 266 280 260 A12 12 0 0 1 304 260 C304 266 300 271 292 282 Z" fill="var(--red)"/>
    <circle cx="292" cy="260" r="4.5" fill="var(--green)"/>
    <g class="icon-phone">
      <circle cx="305" cy="311" r="10" fill="var(--charcoal)"/>
      <path d="M301 305 Q299 311 304 316 Q308 319 310 316 L308 313 L306 314 Q303 311 303 309 L304 307 Z" fill="var(--white)"/>
    </g>
    <g class="icon-web">
      <circle cx="314" cy="339" r="10" fill="var(--charcoal)"/>
      <circle cx="314" cy="339" r="6" fill="none" stroke="var(--white)" stroke-width="1.3"/>
      <ellipse cx="314" cy="339" rx="2.5" ry="6" fill="none" stroke="var(--white)" stroke-width="1.2"/>
      <line x1="308" y1="339" x2="320" y2="339" stroke="var(--white)" stroke-width="1.2"/>
    </g>
  </svg>

  <div class="t brand"><span class="brand-mark"></span>Summit Tile</div>
  <p class="t tagline">Floor installation,<br>sales &amp; service</p>
  <p class="t free">FREE</p>
  <p class="t in-home">In-Home</p>
  <p class="t consult">CONSULTATION</p>
  <p class="t quote">Request a Quote</p>

  <p class="t service s-floors">Floors</p>
  <p class="t service s-cabinets">Cabinets</p>
  <p class="t service s-counter">Countertops</p>
  <p class="t about">We are a retail and wholesale business selling premium flooring, ready to assemble cabinets, and granite countertops.</p>
  <p class="t here">WE ARE HERE</p>
  <p class="t address">417 W. Hwy 82, Duncanville, TX 75284</p>
  <p class="t phone">972-8-TILEUP (972-845-3887)</p>
  <p class="t web">www.summittilehub.example</p>
</section>
</body>
</html>
```